Consulting Company Business Card

I am looking for a minimalist, classy, professional design on my business card. I would like it to be double-sided. I want to use the font and color scheme of my logo which are attached. Please be creative in the designs that you send me. I want to play off the design of my logo with the inner C that is Green and Blue broken up with the white.
Target Market(s)
Small Businesses
Industry/Entity Type
Consulting
Contact Information for Business Card
Dale M. Whitcombe, CPA CGMA, 555-014-2873, dwhitcombe@vorantaadvisory.example, www.vorantaadvisory.example

```html
<!DOCTYPE html>
<html lang="en">
<head>
<meta charset="utf-8">
<title>Voranta Advisory — Business Card</title>
<link href="https://fonts.googleapis.com/css2?family=Montserrat:wght@400;500;700;800&display=swap" rel="stylesheet">
<style>
  :root {
    --teal: #2a8589;
    --teal-light: #30969a;
    --navy: #2b2f5a;
    --ink: #1f2230;
    --paper: #ffffff;
    --backdrop: #e6e8ea;
  }
  * { box-sizing: border-box; margin: 0; padding: 0; }
  html, body {
    width: 1200px; height: 960px; overflow: hidden;
    background: var(--backdrop);
    font-family: "Montserrat", sans-serif;
  }
  .canvas {
    width: 1200px; height: 960px;
    display: flex; flex-direction: column; align-items: center; justify-content: center;
    gap: 30px;
  }
  .card {
    position: relative;
    width: 760px; height: 434px;
    border-radius: 26px;
    overflow: hidden;
    box-shadow: 0 6px 18px rgba(0,0,0,.12);
  }

  /* Front */
  .card--front {
    background: linear-gradient(135deg, var(--teal-light), var(--teal));
    display: flex; align-items: center; justify-content: center;
  }
  .brand { display: flex; align-items: center; gap: 18px; }
  .brand__dot { width: 22px; height: 22px; border-radius: 50%; }
  .brand__name {
    font-weight: 800; text-transform: uppercase; line-height: 1.05;
  }
  .card--front .brand__dot { background: var(--paper); }
  .card--front .brand__name { color: var(--paper); font-size: 50px; letter-spacing: 2px; }

  /* Back */
  .card--back { background: var(--paper); }
  .card__wave { position: absolute; left: 0; bottom: 0; width: 760px; height: 434px; }
  .back__brand {
    position: absolute; left: 56px; top: 120px; width: 250px;
  }
  .card--back .brand__dot { background: var(--teal); width: 16px; height: 16px; }
  .card--back .brand__name { color: var(--navy); font-size: 32px; letter-spacing: 1px; }
  .back__divider {
    position: absolute; left: 330px; top: 78px; width: 2px; height: 150px;
    background: var(--teal);
  }
  .contact {
    position: absolute; left: 362px; top: 74px;
  }
  .contact__name {
    color: var(--teal); font-weight: 800; font-size: 20px;
    text-transform: uppercase; letter-spacing: .5px;
  }
  .contact__title { color: var(--ink); font-weight: 500; font-size: 15px; margin-top: 4px; }
  .contact__list { list-style: none; margin-top: 16px; }
  .contact__item {
    display: flex; align-items: center; gap: 12px;
    color: var(--ink); font-size: 14px; margin-bottom: 9px;
  }
  .contact__icon { width: 16px; height: 16px; flex: none; }
</style>
</head>
<body>
<main class="canvas">
  <section class="card card--front">
    <div class="brand">
      <span class="brand__dot"></span>
      <p class="brand__name">Voranta<br>Advisory</p>
    </div>
  </section>

  <section class="card card--back">
    <svg class="card__wave" viewBox="0 0 760 434" aria-hidden="true">
      <path d="M0,404 C200,384 330,344 420,304 C560,244 660,212 760,206 L760,434 L0,434 Z" fill="var(--teal)"/>
      <path d="M0,392 C200,372 330,332 420,292 C560,232 660,196 760,190" fill="none" stroke="var(--navy)" stroke-width="6"/>
    </svg>

    <div class="back__brand brand">
      <span class="brand__dot"></span>
      <p class="brand__name">Voranta<br>Advisory</p>
    </div>

    <div class="back__divider"></div>

    <div class="contact">
      <p class="contact__name">Dale M. Whitcombe</p>
      <p class="contact__title">CPA CGMA</p>
      <ul class="contact__list">
        <li class="contact__item">
          <svg class="contact__icon" viewBox="0 0 24 24"><path fill="var(--teal)" d="M6.6 10.8a15.1 15.1 0 0 0 6.6 6.6l2.2-2.2c.3-.3.7-.4 1-.2 1.1.4 2.3.6 3.6.6.6 0 1 .4 1 1V20c0 .6-.4 1-1 1A17 17 0 0 1 3 4c0-.6.4-1 1-1h3.5c.6 0 1 .4 1 1 0 1.3.2 2.5.6 3.6.1.3 0 .7-.2 1z"/></svg>
          555-014-2873
        </li>
        <li class="contact__item">
          <svg class="contact__icon" viewBox="0 0 24 24"><rect x="2" y="5" width="20" height="14" rx="2" fill="var(--teal)"/><path d="M3 6l9 7 9-7" fill="none" stroke="#fff" stroke-width="1.8"/></svg>
          dwhitcombe@vorantaadvisory.example
        </li>
        <li class="contact__item">
          <svg class="contact__icon" viewBox="0 0 24 24"><circle cx="12" cy="12" r="10" fill="var(--teal)"/><path d="M2 12h20M12 2c3 3 3 17 0 20M12 2c-3 3-3 17 0 20" fill="none" stroke="#fff" stroke-width="1.4"/></svg>
          www.vorantaadvisory.example
        </li>
      </ul>
    </div>
  </section>
</main>
</body>
</html>
```